We need a flyer where we promote a workshop to our members of the jewish community www.vbq-gemeinde.example . The workshop is calles "command in seven weeks presented by VBQ. We would like to see a flyer with the below text is used and also some pictures (attached). The flyer should come over as cool, fresh, innovative for a younger crowd so called young professionals (age 28-35).
TITLE.
"Command in Seven Weeks.
SUBTITLE.
Your systematic self-coaching roadmap to power and impact—and your future.”
TEXT.
Dr. Marcus L. Brandauer is the CEO Emeritus of Alpine Advisory Partners—he made an exit in 2013. He is the award-winning author of 8 books, including "Momentum-By-Design," "Speak Up or Fade" and "The Cantor and the Chairman.”
For the past 20 years he has taught leadership at Harwick University in New York and at KLB (Lindmoor University) to prepare future CEOs and other leaders in business, government , nonprofits and the military.
Now, in a process exclusively designed for VBQ’s next generation of emerging leaders, Marcus unpacks his leadership secrets in 3 action-packed labs—reduced to the max:
Lab 1. Command in Seven Weeks: The Summit Compass Model®. Self-Assessment. Self-Leadership: “The Lantern.” 5-Year Vision. 100-Day Catalytic Project.
Lab 2. Guiding Through Words. Relationship: Building Trust. Momentum-By-Design. Cockpit.
Lab 3. Debrief and Scale-Up. Sustainability. Action Tools.
Do you want to build your own future and a life you love? Do you want to jump-start that future and life over 100 days while learning a toolbox of leadership skills, networking with like-minded people—and even get some pizza? Then join us.
young professionals age 28-35

```html
<!DOCTYPE html>
<html lang="en">
<head>
<meta charset="utf-8">
<title>Command in Seven Weeks – VBQ Workshop Flyer</title>
<link rel="stylesheet" href="https://fonts.googleapis.com/css2?family=Bebas+Neue&family=Rubik:wght@400;500;700&family=Source+Sans+3:wght@400;600;700&display=swap">
<style>
  :root {
    --ink: #0a0c12;
    --cyan: #4cc9ea;
    --cyan-light: #66d6f2;
    --blue: #1f6fc1;
    --blue-deep: #174f9e;
    --navy: #0f2d6b;
    --navy-dark: #0b2258;
    --pale: #c5e4f6;
    --white: #ffffff;
    --text-dark: #1a2d55;
  }
  * { margin: 0; padding: 0; box-sizing: border-box; }
  html, body { width: 720px; height: 1200px; overflow: hidden; background: var(--white); }
  .flyer { position: relative; width: 720px; height: 1200px; overflow: hidden; background: var(--white); font-family: "Source Sans 3", sans-serif; }
  .abs { position: absolute; }

  .event-photo { left: 0; top: 0; width: 720px; height: 628px;
    background: radial-gradient(ellipse at 72% 28%, #3a2a2e 0%, #1a1c26 35%, #0c0e16 70%), var(--ink); }
  .left-dark { left: 0; top: 0; width: 418px; height: 506px; background: linear-gradient(180deg, #0a0b10 0%, #11141c 100%); }

  .title { left: 41px; top: 40px; color: var(--white); font-family: "Bebas Neue", sans-serif; font-weight: 400; }
  .title-line1 { display: flex; align-items: center; gap: 8px; font-size: 80px; line-height: 1; transform: scaleY(1.15); transform-origin: top left; letter-spacing: -0.5px; }
  .title-in { background: var(--cyan); color: var(--white); font-size: 64px; line-height: 1; padding: 2px 6px 0; }
  .title-line2 { display: block; color: var(--cyan); font-size: 92px; line-height: 1; letter-spacing: -1px; transform: scaleY(1.3); transform-origin: top left; margin-top: 4px; }

  .subtitle-panel { left: 41px; top: 288px; width: 377px; height: 218px; background: var(--blue); }
  .subtitle { left: 67px; top: 306px; width: 345px; color: var(--white); font-family: "Rubik", sans-serif; font-weight: 500; font-size: 25px; line-height: 40px; }

  .bio-panel { left: 41px; top: 506px; width: 377px; height: 694px; background: linear-gradient(180deg, var(--blue-deep) 0%, var(--navy) 45%, var(--navy-dark) 100%); }
  .side-strip-cyan { left: 0; top: 558px; width: 41px; height: 100px; background: var(--cyan-light); }

  .bio { left: 67px; top: 518px; width: 335px; color: var(--white); font-size: 14.5px; line-height: 20.5px; }
  .bio p { margin-bottom: 16px; }
  .bio .name { color: var(--cyan); font-weight: 700; }
  .bio .lead-in { color: var(--cyan); font-weight: 700; }

  .portrait { left: -40px; top: 856px; }

  .book-photo { left: 445px; top: 299px; width: 245px; height: 330px;
    background: linear-gradient(160deg, #d8332a 0%, #b8201a 55%, #6e120f 100%); }

  .labs { left: 418px; top: 628px; width: 302px; height: 248px; background: var(--white); }
  .lab { position: absolute; left: 30px; width: 262px; display: flex; gap: 10px; font-size: 13.5px; line-height: 19px; color: var(--text-dark); }
  .lab svg { flex: 0 0 18px; margin-top: 1px; }
  .lab b { color: var(--blue); font-weight: 700; }

  .invite { left: 418px; top: 876px; width: 302px; height: 151px; background: var(--cyan-light); }
  .invite p { position: absolute; left: 19px; top: 16px; width: 270px; font-weight: 700; font-size: 13.5px; line-height: 19px; color: var(--navy-dark); }

  .contact { left: 418px; top: 1027px; width: 302px; height: 157px; background: var(--white); font-family: "Rubik", sans-serif; color: var(--text-dark); }
  .contact-row { position: absolute; left: 62px; display: flex; align-items: center; gap: 8px; white-space: nowrap; }
  .contact-row svg { position: absolute; left: -22px; }
  .contact .web { top: 18px; font-weight: 700; font-size: 16px; }
  .contact .phone { top: 50px; font-weight: 700; font-size: 20px; }
  .contact .address { position: absolute; left: 81px; top: 84px; font-size: 15.5px; line-height: 22px; }
  .contact .address svg { position: absolute; left: -22px; top: 3px; }
  .bottom-bar { left: 375px; top: 1184px; width: 345px; height: 16px; background: var(--blue-deep); }

  .brand-badge { z-index: 5; left: 334px; top: 1043px; width: 124px; height: 124px; border-radius: 50%; background: var(--blue); display: flex; align-items: center; justify-content: center; color: var(--white); font-family: "Rubik", sans-serif; font-weight: 700; font-size: 38px; }
</style>
</head>
<body>
<div class="flyer">
  <div class="abs event-photo" role="img" aria-label="Photo of a speaker on a conference stage in front of a large audience"></div>
  <div class="abs left-dark"></div>

  <h1 class="abs title">
    <span class="title-line1">COMMAND <span class="title-in">IN</span></span>
    <span class="title-line2">SEVEN WEEKS</span>
  </h1>

  <div class="abs book-photo" role="img" aria-label="Photo of two red book covers titled Command in Seven Weeks"></div>

  <div class="abs subtitle-panel"></div>
  <h2 class="abs subtitle">Your systematic<br>self-coaching roadmap to<br>power and impact—and<br>your future.</h2>

  <div class="abs side-strip-cyan"></div>
  <div class="abs bio-panel"></div>

  <div class="abs bio">
    <p><span class="name">Dr. Marcus L. Brandauer</span> is the CEO Emeritus of Alpine Advisory Partners—he made an exit in 2013. He is the award-winning author of 8 books, including "Momentum-By-Design," "Speak Up or Fade" and "The Cantor and the Chairman."</p>
    <p>For the past 20 years he has taught leadership at Harwick University in New York and at KLB (Lindmoor University) to prepare future CEOs and other leaders in business, government, nonprofits and the military.</p>
    <p class="lead-in">Now, in a process exclusively designed for VBQ’s next generation of emerging leaders, Marcus unpacks his leadership secrets in 3 action-packed labs—reduced to the max:</p>
  </div>

  <svg class="abs portrait" width="480" height="480" viewBox="0 0 480 480" role="img" aria-label="Portrait photo of the speaker, smiling, in a dark blazer">
    <circle cx="240" cy="240" r="222" fill="var(--pale)" stroke="#2a6fc4" stroke-width="22"/>
  </svg>

  <div class="abs labs">
    <div class="lab" style="top:15px">
      <svg width="18" height="18" viewBox="0 0 18 18"><circle cx="9" cy="9" r="7.5" fill="none" stroke="var(--blue)" stroke-width="1.6"/><path d="M5 9.2l3 3 6-7" fill="none" stroke="var(--blue)" stroke-width="1.8" stroke-linecap="round"/></svg>
      <span><b>Lab 1</b>. Command in Seven Weeks: The Summit Compass Model®. Self-Assessment. Self-Leadership: “The Lantern.” 5-Year Vision. 100-Day Catalytic Project.</span>
    </div>
    <div class="lab" style="top:125px">
      <svg width="18" height="18" viewBox="0 0 18 18"><circle cx="9" cy="9" r="7.5" fill="none" stroke="var(--blue)" stroke-width="1.6"/><path d="M5 9.2l3 3 6-7" fill="none" stroke="var(--blue)" stroke-width="1.8" stroke-linecap="round"/></svg>
      <span><b>Lab 2</b>. Guiding Through Words. Relationship: Building Trust. Momentum-By-Design. Cockpit.</span>
    </div>
    <div class="lab" style="top:195px">
      <svg width="18" height="18" viewBox="0 0 18 18"><circle cx="9" cy="9" r="7.5" fill="none" stroke="var(--blue)" stroke-width="1.6"/><path d="M5 9.2l3 3 6-7" fill="none" stroke="var(--blue)" stroke-width="1.8" stroke-linecap="round"/></svg>
      <span><b>Lab 3</b>. Debrief and Scale-Up. Sustainability. Action Tools.</span>
    </div>
  </div>

  <div class="abs invite">
    <p>Do you want to build your own future and a life you love? Do you want to jump-start that future and life over 100 days while learning a toolbox of leadership skills, networking with like-minded people—and even get some pizza? Then join us.</p>
  </div>

  <div class="abs contact">
    <div class="contact-row web">
      <svg width="15" height="15" viewBox="0 0 16 16"><circle cx="8" cy="8" r="6.5" fill="none" stroke="var(--blue)" stroke-width="1.5"/><ellipse cx="8" cy="8" rx="2.8" ry="6.5" fill="none" stroke="var(--blue)" stroke-width="1.3"/><path d="M1.5 8h13M2.5 4.8h11M2.5 11.2h11" stroke="var(--blue)" stroke-width="1.2"/></svg>
      www.vbq-gemeinde.example
    </div>
    <div class="contact-row phone">
      <svg width="15" height="15" viewBox="0 0 16 16"><path d="M3.5 1.5l2.5 0 1.2 3.2-1.6 1.2a8 8 0 0 0 4.5 4.5l1.2-1.6 3.2 1.2v2.5c0 .8-.7 1.5-1.5 1.5A12.5 12.5 0 0 1 2 3c0-.8.7-1.5 1.5-1.5z" fill="var(--blue)"/></svg>
      +41 44 555 01 90
    </div>
    <div class="address">
      <svg width="13" height="17" viewBox="0 0 13 17"><path d="M6.5 0A6 6 0 0 0 .5 6c0 4.5 6 11 6 11s6-6.5 6-11a6 6 0 0 0-6-6zm0 8.5a2.5 2.5 0 1 1 0-5 2.5 2.5 0 0 1 0 5z" fill="var(--blue)"/></svg>
      VBQ community center<br>Lindenhofweg 12<br>8001 Zurich
    </div>
  </div>
  <div class="abs bottom-bar"></div>

  <div class="abs brand-badge">VBQ</div>
</div>
</body>
</html>
```